We need a book cover that resonates with the everyday parent. It should represent family, diversity, and accountability. Our new book "The DOVE Pathway: A Handbook for the Modern-Day Parent" represents a new method in parenting where the parent is the focus of change. Book will be sold on Brindlemart, Pagevault, quillo, as well as on the shelf.
Required elements are:
The Title: The DOVE Pathway: A Handbook for the Modern-Day Parent
The Authors: Harold J. Pemberly, M.Ed. and Lucas R. Fennimore
Our Logo: See attached file - the logo should be present, but not predominant
Visit our website www.dovegroupsite.example for more background on DOVE.

```html
<!DOCTYPE html>
<html lang="en">
<head>
<meta charset="utf-8">
<title>The DOVE Pathway: A Handbook for the Modern-Day Parent</title>
<link rel="stylesheet" href="https://fonts.googleapis.com/css2?family=Cinzel:wght@400;500&family=Arimo:wght@700&family=Cabin+Sketch:wght@700&display=swap">
<style>
  :root {
    --page: #ffffff;
    --cover: #ffffff;
    --green: #6cb022;
    --ink: #111111;
    --band-text: #ffffff;
    --photo-light: #eef0f2;
    --photo-mid: #b9c6d6;
    --photo-deep: #5b7495;
  }
  * { margin: 0; padding: 0; box-sizing: border-box; }
  html, body {
    width: 1000px;
    height: 1200px;
    overflow: hidden;
    background: var(--page);
  }
  .cover {
    position: absolute;
    left: 152px;
    top: 38px;
    width: 748px;
    height: 1124px;
    background: var(--cover);
    border: 1px solid #e4e4e4;
  }
  .band {
    position: absolute;
    left: 0;
    width: 100%;
    background: var(--green);
    color: var(--band-text);
    font-family: "Cinzel", "Times New Roman", serif;
    font-weight: 400;
    text-align: center;
    letter-spacing: 1px;
  }
  .band--top {
    top: 0;
    height: 68px;
    font-size: 36px;
    line-height: 70px;
  }
  .band--bottom {
    bottom: 0;
    height: 70px;
    font-size: 37px;
    line-height: 74px;
  }
  .title-main {
    position: absolute;
    left: 0;
    top: 148px;
    width: 100%;
    padding-left: 72px;
    font-family: "Arimo", Arial, sans-serif;
    font-weight: 700;
    font-size: 60px;
    letter-spacing: -0.5px;
    color: var(--ink);
    white-space: nowrap;
  }
  .title-main .brand-name {
    color: var(--ink);
  }
  .cover-photo {
    position: absolute;
    left: 18px;
    top: 262px;
    width: 222px;
    height: 790px;
    background: linear-gradient(180deg, var(--photo-light) 0%, var(--photo-mid) 40%, var(--photo-deep) 85%, var(--photo-light) 100%);
    border-radius: 4px;
  }
  .subtitle {
    position: absolute;
    left: 240px;
    top: 300px;
    width: 488px;
    font-family: "Cabin Sketch", "Comic Sans MS", cursive;
    font-weight: 700;
    color: var(--green);
    text-align: center;
  }
  .subtitle__line {
    display: block;
    font-size: 112px;
    line-height: 132px;
  }
  .subtitle__line--long {
    font-size: 82px;
  }
</style>
</head>
<body>
  <main class="cover">
    <div class="band band--top">Harold J. Pemberly, M.Ed.</div>

    <h1 class="title-main">The <span class="brand-name">DOVE</span> Pathway:</h1>

    <div class="cover-photo" role="img" aria-label="Photo of a smiling child in a denim shirt and jeans peeking out from behind a white panel"></div>

    <h2 class="subtitle">
      <span class="subtitle__line subtitle__line--long">A Handbook</span>
      <span class="subtitle__line">for the</span>
      <span class="subtitle__line">Modern-</span>
      <span class="subtitle__line">Day</span>
      <span class="subtitle__line">Parent</span>
    </h2>

    <div class="band band--bottom">Lucas R. Fennimore</div>
  </main>
</body>
</html>
```